Graphics for Blog Post Series

We are looking for 3 infographic style designs (see attached examples) to be used in a blog post series about CDL training. This blog post series includes 3 separate posts (links provided below) and the graphics should have a consistent look and feel across all 3 posts.

The point of each graphic is to have a visual representation of content discussed in each post and tell the story of that post. It should be something that will allow people to get an idea of what the post is about by looking at a visual.

The 3 mini graphics can be used independently with each post or all as one larger image that flows together (as shown in the attached example)

The size of each individual image should be 802 X 372. The size of all images put together (stacked on top of each other) should be 802 X 1117

Blog Post #1: http://brightroutelessons.example/blog/top-10-reasons-to-choose-company-sponsored-cdl-training/

Ideas for graphic: some type of graphic to represent a Top 10 List with a couple numbers and examples from the post. Text can be used to make the purpose of the image clear (as shown in example)

Blog Post #2: http://brightroutelessons.example/blog/pay-for-cdl-training/

Ideas for graphic: graphic showing money being held up (possibly by a person's hand) and words "How to pay for CDL training"

Blog Post #3: http://brightroutelessons.example/blog/cdl-job-opportunity/

Ideas for graphic: show a truck (similar to one in pitfall example) with a flat tire and indicate visually that a CDL with no job isn't going anywhere.

Again, we want these graphics to be very similar to the examples attached as they will be used in the same manner.

```html
<!DOCTYPE html>
<html lang="en">
<head>
<meta charset="utf-8">
<title>CDL Training Blog Series Graphics</title>
<link rel="stylesheet" href="https://fonts.googleapis.com/css2?family=Source+Sans+3:ital,wght@0,600;0,700;1,700&display=swap">
<style>
  :root {
    --green: #58b947;
    --green-dark: #3f9c3c;
    --green-deep: #2f7f33;
    --yellow: #f8ca6c;
    --yellow-soft: #f6d28a;
    --white: #ffffff;
  }
  * { margin: 0; padding: 0; box-sizing: border-box; }
  html, body { width: 1200px; height: 836px; overflow: hidden; background: var(--white); }
  body { font-family: "Source Sans 3", "Helvetica Neue", Arial, sans-serif; }
  .series { position: relative; width: 1200px; height: 836px; background: var(--white); }
  .panel { position: absolute; top: 0; height: 836px; overflow: hidden; }
  .panel--reasons { left: 0; width: 386px; background: linear-gradient(var(--green) 0 474px, var(--yellow) 474px); }
  .panel--pay { left: 406px; width: 388px; background: linear-gradient(var(--green) 0 438px, var(--yellow) 438px); }
  .panel--job { left: 814px; width: 386px; background: linear-gradient(var(--yellow) 0 234px, var(--green) 234px); }

  .art { position: absolute; }
  .art--graduate { left: 112px; top: 24px; width: 176px; height: 170px; border-radius: 80px 80px 20px 20px; background: linear-gradient(var(--yellow-soft), var(--yellow)); }
  .art--cash { left: 40px; top: 0; width: 276px; height: 414px; border-radius: 0 0 40px 40px; background: linear-gradient(160deg, var(--yellow-soft), var(--yellow) 60%, var(--white)); opacity: .9; }
  .art--climb { left: 60px; top: 10px; width: 262px; height: 224px; background: linear-gradient(var(--green-dark), var(--green)); border-radius: 4px; }
  .art--truck { left: 0; top: 578px; width: 386px; height: 258px; border-radius: 18px 18px 0 0; background: linear-gradient(180deg, var(--yellow-soft) 0%, var(--yellow) 72%, var(--green-dark) 100%); }

  .sign { position: absolute; left: 54px; top: 180px; width: 268px; height: 334px; background: var(--white); border: 7px solid var(--green-dark); border-radius: 6px; display: flex; flex-direction: column; align-items: center; justify-content: center; text-align: center; color: var(--green-dark); }
  .sign__title { font-weight: 700; font-size: 38px; line-height: 49px; }
  .sign__note { font-weight: 700; font-size: 21px; letter-spacing: -0.8px; line-height: 40px; }

  .reasons-list { position: absolute; left: 26px; top: 529px; width: 299px; list-style: none; color: var(--green-deep); font-style: italic; font-weight: 700; font-size: 16.5px; letter-spacing: 0.2px; line-height: 22.2px; counter-reset: reason; }
  .reasons-list li { position: relative; padding-left: 36px; counter-increment: reason; }
  .reasons-list li::before { content: counter(reason) "."; position: absolute; left: 0; }

  .pay-title { position: absolute; left: 0; top: 464px; width: 388px; text-align: center; color: var(--green-dark); font-weight: 700; font-size: 60px; line-height: 67px; }

  .job-title { position: absolute; left: 0; top: 264px; width: 386px; text-align: center; color: var(--white); font-weight: 700; font-size: 46px; line-height: 56.4px; }
</style>
</head>
<body>
<main class="series">
  <section class="panel panel--reasons">
    <div class="art art--graduate" role="img" aria-label="Illustration of a graduate in a cap holding up a sign"></div>
    <div class="sign">
      <p class="sign__title">Top 10<br>Reasons<br>to Choose</p>
      <p class="sign__note">(Company Sponsored)</p>
      <p class="sign__title">CDL<br>Training?</p>
    </div>
    <ol class="reasons-list">
      <li>Job opportunity before training</li>
      <li>Don't have enough money to pay for CDL training</li>
      <li>No credit checks</li>
      <li>No upfront tuition costs</li>
      <li>No loans, no interest</li>
      <li>Training from a reputable truck driving school</li>
      <li>Want to learn from instructors with proven experience</li>
      <li>Able to start a new career quickly</li>
      <li>Meet fellow drivers/teammates</li>
      <li>Other</li>
    </ol>
  </section>

  <section class="panel panel--pay">
    <div class="art art--cash" role="img" aria-label="Illustration of a hand holding up a stack of paper money"></div>
    <h2 class="pay-title">How<br>to pay<br>for<br>CDL<br>training</h2>
  </section>

  <section class="panel panel--job">
    <div class="art art--climb" role="img" aria-label="Illustration of two figures helping each other climb a rising arrow chart"></div>
    <h2 class="job-title">A CDL<br>without a job<br>opportunity<br>is like a truck<br>with a flat tire</h2>
    <div class="art art--truck" role="img" aria-label="Illustration of a semi truck with a flat tire"></div>
  </section>
</main>
</body>
</html>
```